Cafe & Organic Juicery in Pasadena CA

these pages need to be accessible and mobile friendly.
Pasadena mountains, the rose symbol or city design incorporated , Brick features incorporated into website since . Rustic Golds incorporated with the brick . ill attach reference pictures
Updates

Reference websites: Tidewrenpantry.example Thesaddlersniece.example Quincebarco.example

Also in the logo itself please make font on Cafe & organic match the Juicery below. It seems that it’s just a juicery due the bold writing

There is an updated version of the logo that was just added by Marlon . Please use that one with black. BAckround ( white bAckround ok at bottom of page )

Coding

Coded - Design and coding required

Number of Pages Required

5+ page

Requirements
Must have
• Mobile Friendly and functionality
• Main Page & the following pages : As tabs the brick below is from harbin stone supply and will be used for wall decoration
• Delivery Orders
• Pick up Orders / Reservations
• Menu
• Our Kombucha
• Our Coffee & Fresh pressed Juices
• About us
Nice to have
• Phone number and address should be located nicely on top of page with option to click on from mobile phones to call
• Tabs that direct to the pages referenced above should be located and easily found on the top of the main page & visible from website or mobile phone.

```html
<!DOCTYPE html>
<html lang="en">
<head>
<meta charset="utf-8">
<title>Verra Cafe &amp; Organic Juicery</title>
<link rel="stylesheet" href="https://fonts.googleapis.com/css2?family=Cinzel:wght@400;700&family=Oswald:wght@400;500&family=Open+Sans:wght@400;600&display=swap">
<style>
:root{
  --green:#3f7a4a;
  --green-dark:#2f5a37;
  --green-btn:#6aa77a;
  --gold:#c98f2e;
  --gold-dark:#a56f1c;
  --ink:#333333;
  --grey:#6b6b6b;
  --mist:#e6e9e7;
  --white:#ffffff;
}
*{box-sizing:border-box;margin:0;padding:0}
html,body{width:1200px;height:2773px;overflow:hidden}
body{position:relative;background:var(--white);font-family:"Open Sans",sans-serif;color:var(--ink)}
a{color:inherit;text-decoration:none}
.abs{position:absolute}

/* header */
.site-header{position:absolute;left:0;top:0;width:1200px;height:113px;background:var(--white);z-index:3}
.brand{position:absolute;left:129px;top:6px;width:148px;height:148px;border-radius:50%;background:var(--white);box-shadow:0 2px 6px rgba(0,0,0,.25);display:flex;align-items:center;justify-content:center}
.brand-ring{position:absolute;inset:10px;border-radius:50%;border:3px solid var(--green)}
.brand-name{font-family:"Cinzel",serif;font-weight:700;font-size:32px;color:var(--green)}
.contact-bar{position:absolute;top:16px;left:500px;display:flex;gap:36px;font-family:"Oswald",sans-serif;font-size:15px;color:#444;align-items:center}
.contact-bar span{display:flex;align-items:center;gap:6px}
.cart{position:absolute;left:958px;top:5px;width:107px;height:37px;background:var(--green-btn);color:var(--white);font-family:"Oswald",sans-serif;font-size:15px;display:flex;align-items:center;justify-content:center;gap:6px}
.main-nav{position:absolute;top:68px;left:296px;display:flex;gap:23px;font-family:"Oswald",sans-serif;font-size:15.5px;color:#666;text-transform:uppercase;letter-spacing:.2px}

/* hero */
.hero{position:absolute;left:0;top:113px;width:1200px;height:627px;background:linear-gradient(180deg,#5f6a7c 0%,#7d7476 30%,#6b5a55 52%,#3d2c28 72%,#1e1614 100%)}
.hero-title{position:absolute;top:222px;width:100%;text-align:center;font-family:"Cinzel",serif;font-size:58px;color:var(--white);letter-spacing:1px}
.hero-sub{position:absolute;top:292px;width:100%;text-align:center;font-family:"Cinzel",serif;font-size:32px;color:var(--white);letter-spacing:1px}
.btn-outline{position:absolute;border:2px solid var(--white);color:var(--white);font-family:"Oswald",sans-serif;font-size:18px;display:flex;align-items:center;justify-content:center;letter-spacing:.5px}

/* about */
.about{position:absolute;left:0;top:740px;width:1200px;height:517px;background:linear-gradient(180deg,#d59a3a,#c6872b 55%,#b97a22)}
.about-photo{position:absolute;left:189px;top:68px;width:362px;height:364px;border-radius:10px;background:radial-gradient(circle at 55% 45%,#b58a60,#5a3b26 55%,#2a1c14)}
.about-title{position:absolute;left:612px;top:100px;font-family:"Cinzel",serif;font-size:40px;color:var(--white)}
.about-text{position:absolute;left:614px;top:158px;width:450px;font-size:15px;line-height:27px;color:var(--white)}

/* menu */
.menu{position:absolute;left:0;top:1257px;width:1200px;height:603px;background:var(--white)}
.menu-bg{position:absolute;left:0;bottom:0;width:1200px;height:330px;background:linear-gradient(180deg,rgba(230,233,231,0) 0%,#e9ebea 40%,#dfe2e0 100%)}
.section-title{position:absolute;top:42px;width:100%;text-align:center;font-family:"Cinzel",serif;font-size:32px;color:var(--ink)}
.menu-item{position:absolute;top:120px;width:300px;text-align:center}
.menu-visual{position:relative;width:300px;height:300px;margin:0 auto}
.menu-photo{position:absolute;left:28px;top:28px;width:244px;height:244px;border-radius:50%}
.menu-name{font-family:"Cinzel",serif;font-size:28px;color:var(--green);margin-top:2px}
.menu-desc{font-size:14px;line-height:20px;color:var(--grey);width:240px;margin:2px auto 0}
.chev{width:30px;height:30px;border-radius:50%;background:var(--green);margin:10px auto 0;display:flex;align-items:center;justify-content:center}

/* promo */
.promo{position:absolute;left:0;top:1860px;width:1200px;height:510px;background:linear-gradient(90deg,#7a1a1c 0%,#b8402a 20%,#6b5a3a 45%,#3f3a2c 65%,#7e9a3a 82%,#6e5332 100%)}
.promo-frame{position:absolute;left:270px;top:133px;width:629px;height:244px;border:8px solid var(--white);background:rgba(0,0,0,.28)}
.promo-title{position:absolute;top:40px;width:100%;text-align:center;font-family:"Cinzel",serif;font-size:36px;color:var(--white)}
.promo-text{position:absolute;top:88px;width:100%;text-align:center;font-size:16px;line-height:26px;color:var(--white)}

/* footer */
.site-footer{position:absolute;left:0;top:2370px;width:1200px;height:403px;background:linear-gradient(180deg,#ffffff 0%,#f2f4f3 40%,#d9dedb 100%)}
.footer-brand{position:absolute;left:154px;top:77px;width:136px;height:136px;border-radius:50%;background:var(--white);box-shadow:0 2px 6px rgba(0,0,0,.25);display:flex;align-items:center;justify-content:center}
.footer-brand .brand-ring{inset:8px}
.footer-brand .brand-name{font-size:28px}
.footer-col{position:absolute;top:85px}
.footer-col h3{font-family:"Cinzel",serif;font-weight:400;font-size:18px;color:var(--green);margin-bottom:10px}
.footer-col li{list-style:none;font-size:14px;line-height:24.5px;color:#444;padding-left:4px}
.contact-list li{display:flex;gap:10px;align-items:flex-start}
.social{display:flex;gap:8px;margin-top:14px}
.social span{width:27px;height:27px;border-radius:50%;border:1.5px solid var(--green)}
.footer-rule{position:absolute;left:170px;right:170px;top:335px;border-top:1px solid #b9bfbb}
.copyright{position:absolute;top:356px;width:100%;text-align:center;font-size:11px;color:#555}
</style>
</head>
<body>

<header class="site-header">
  <a class="brand" href="#" aria-label="Verra Cafe and Organic Juicery home"><span class="brand-ring"></span><span class="brand-name">Verra</span></a>
  <div class="contact-bar">
    <span><svg width="16" height="16" viewBox="0 0 24 24"><path fill="#3f7a4a" d="M6.6 10.8a15 15 0 0 0 6.6 6.6l2.2-2.2a1 1 0 0 1 1-.25 11.4 11.4 0 0 0 3.6.57 1 1 0 0 1 1 1V20a1 1 0 0 1-1 1A17 17 0 0 1 3 4a1 1 0 0 1 1-1h3.5a1 1 0 0 1 1 1c0 1.25.2 2.45.57 3.57a1 1 0 0 1-.25 1z"/></svg><a href="tel:6265550148">(626) 555 0148</a></span>
    <span><svg width="14" height="18" viewBox="0 0 24 30"><path fill="#3f7a4a" d="M12 0a10 10 0 0 0-10 10c0 7.5 10 20 10 20s10-12.5 10-20A10 10 0 0 0 12 0zm0 14a4 4 0 1 1 0-8 4 4 0 0 1 0 8z"/></svg>42 ORCHARD LANE #B PASADENA CA 91101</span>
  </div>
  <a class="cart" href="#"><svg width="20" height="18" viewBox="0 0 24 22"><path fill="none" stroke="#fff" stroke-width="2" d="M1 2h4l3 12h12l3-9H7"/><circle cx="10" cy="19" r="2" fill="#fff"/><circle cx="18" cy="19" r="2" fill="#fff"/></svg>0 ITEMS</a>
  <nav class="main-nav">
    <a href="#">Delivery Orders</a><a href="#">Pick up Orders</a><a href="#">Menu</a><a href="#">Our Kombucha</a><a href="#">Our Coffee &amp; Fresh Pressed Juices</a><a href="#">About Us</a>
  </nav>
</header>

<section class="hero" role="img" aria-label="Palm trees against the San Gabriel mountains at dusk">
  <svg class="abs" style="left:96px;top:250px" width="30" height="56" viewBox="0 0 30 56"><path d="M27 2 3 28l24 26" fill="none" stroke="#fff" stroke-width="3"/></svg>
  <svg class="abs" style="left:1076px;top:250px" width="30" height="56" viewBox="0 0 30 56"><path d="M3 2l24 26L3 54" fill="none" stroke="#fff" stroke-width="3"/></svg>
  <h1 class="hero-title">WELCOME TO VERRA</h1>
  <p class="hero-sub">CAFE &amp; ORGANIC JUICERY</p>
  <a class="btn-outline" href="#" style="left:505px;top:351px;width:183px;height:43px">ORDER NOW</a>
</section>

<section class="about">
  <div class="about-photo" role="img" aria-label="Cup of coffee on a saucer with coffee beans"></div>
  <h2 class="about-title">ABOUT VERRA</h2>
  <p class="about-text">Aed diam Donec quis mi sed magna hendrerit accumsan Suspendisse risus nibh ultricies eu volutpat non condimentum hendrerit augue Etiam eleifend metus vitae adipiscing<br>Maecenas aliquet velit vel turpis Mauris neque metus malesuada nec ultricies sit amet porttitor mattis enim In massa libero interdum nec interdum vel blandit sed nulla</p>
  <a class="btn-outline" href="#" style="left:614px;top:349px;width:183px;height:41px">READ MORE</a>
</section>

<section class="menu">
  <div class="menu-bg" role="img" aria-label="Faint misty mountain and pine tree silhouette"></div>
  <h2 class="section-title">OUR MENU</h2>
  <svg class="abs" style="left:92px;top:240px" width="26" height="50" viewBox="0 0 26 50"><path d="M24 2 3 25l21 23" fill="none" stroke="#333" stroke-width="2.5"/></svg>
  <svg class="abs" style="left:1088px;top:240px" width="26" height="50" viewBox="0 0 26 50"><path d="M2 2l21 23L2 48" fill="none" stroke="#333" stroke-width="2.5"/></svg>

  <article class="menu-item" style="left:137px">
    <div class="menu-visual">
      <svg class="abs" style="left:0;top:0" width="300" height="300" viewBox="0 0 300 300"><path d="M40 80A140 140 0 0 1 230 40" fill="none" stroke="#2f5a37" stroke-width="12"/><path d="M262 90A140 140 0 0 1 270 205" fill="none" stroke="#3f7a4a" stroke-width="10"/></svg>
      <div class="menu-photo" role="img" aria-label="Glasses of beet, carrot and green juice" style="background:radial-gradient(circle at 50% 55%,#e2782a,#7a2040 55%,#4d6a2e)"></div>
    </div>
    <h3 class="menu-name">MENU TITLE</h3>
    <p class="menu-desc">Aorttitor mattis enim In massa libero interdum nec interdum vel</p>
    <div class="chev"><svg width="12" height="8" viewBox="0 0 12 8"><path d="M1 1l5 5 5-5" fill="none" stroke="#fff" stroke-width="2"/></svg></div>
  </article>

  <article class="menu-item" style="left:460px">
    <div class="menu-visual">
      <svg class="abs" style="left:0;top:0" width="300" height="300" viewBox="0 0 300 300"><path d="M40 80A140 140 0 0 1 230 40" fill="none" stroke="#2f5a37" stroke-width="12"/><path d="M262 90A140 140 0 0 1 270 205" fill="none" stroke="#3f7a4a" stroke-width="10"/></svg>
      <div class="menu-photo" role="img" aria-label="Latte with foam art in a white cup" style="background:radial-gradient(circle at 50% 50%,#e8d3b4,#b58356 40%,#3b2a20 80%)"></div>
    </div>
    <h3 class="menu-name">MENU TITLE</h3>
    <p class="menu-desc">Aorttitor mattis enim In massa libero interdum nec interdum vel</p>
    <div class="chev"><svg width="12" height="8" viewBox="0 0 12 8"><path d="M1 1l5 5 5-5" fill="none" stroke="#fff" stroke-width="2"/></svg></div>
  </article>

  <article class="menu-item" style="left:775px">
    <div class="menu-visual">
      <svg class="abs" style="left:0;top:0" width="300" height="300" viewBox="0 0 300 300"><path d="M40 80A140 140 0 0 1 230 40" fill="none" stroke="#2f5a37" stroke-width="12"/><path d="M262 90A140 140 0 0 1 270 205" fill="none" stroke="#3f7a4a" stroke-width="10"/></svg>
      <div class="menu-photo" role="img" aria-label="Jars of orange, green and red juice with kiwi" style="background:linear-gradient(90deg,#f0a020,#7ab83a 50%,#d8302a)"></div>
    </div>
    <h3 class="menu-name">MENU TITLE</h3>
    <p class="menu-desc">Aorttitor mattis enim In massa libero interdum nec interdum vel</p>
    <div class="chev"><svg width="12" height="8" viewBox="0 0 12 8"><path d="M1 1l5 5 5-5" fill="none" stroke="#fff" stroke-width="2"/></svg></div>
  </article>
</section>

<section class="promo" role="img" aria-label="Glasses of fresh juice beside a wooden crate of green apples">
  <div class="promo-frame">
    <h2 class="promo-title">TRY OUR ORGANIC JUICE</h2>
    <p class="promo-text">Alandit sed nulla In ullamcorper est eget tempor cursus neque<br>mi consectetuer mi a ultricies massa est sed nisl</p>
    <a class="btn-outline" href="#" style="left:229px;top:153px;width:183px;height:42px">CLICK HERE</a>
  </div>
</section>

<footer class="site-footer">
  <a class="footer-brand" href="#" aria-label="Verra home"><span class="brand-ring"></span><span class="brand-name">Verra</span></a>
  <div class="footer-col" style="left:349px">
    <h3>QUICK LINKS</h3>
    <ul><li>Delivery Orders</li><li>Pick up Orders</li><li>Menu</li><li>Our Kombucha</li></ul>
  </div>
  <div class="footer-col" style="left:564px">
    <h3>RESOURCES</h3>
    <ul><li>Our Coffee &amp; Fresh pressed Juices</li><li>About us</li><li>Contact Us</li></ul>
    <div class="social" aria-label="Social links"><span></span><span></span><span></span><span></span><span></span></div>
  </div>
  <div class="footer-col contact-list" style="left:837px">
    <h3>CONTACT US</h3>
    <ul>
      <li><svg width="12" height="16" viewBox="0 0 24 30" style="margin-top:4px"><path fill="#3f7a4a" d="M12 0a10 10 0 0 0-10 10c0 7.5 10 20 10 20s10-12.5 10-20A10 10 0 0 0 12 0zm0 14a4 4 0 1 1 0-8 4 4 0 0 1 0 8z"/></svg><span>42 Orchard Lane #B Pasadena<br>CA 91101</span></li>
      <li><svg width="14" height="14" viewBox="0 0 24 24" style="margin-top:5px"><path fill="none" stroke="#3f7a4a" stroke-width="2" d="M6.6 10.8a15 15 0 0 0 6.6 6.6l2.2-2.2 4.6 1.3V20A17 17 0 0 1 3 4h3.5l1.3 4.6z"/></svg><span>626.555.0172</span></li>
      <li><svg width="14" height="12" viewBox="0 0 24 18" style="margin-top:6px"><rect x="1" y="1" width="22" height="16" fill="none" stroke="#3f7a4a" stroke-width="2"/><path d="M1 1l11 9 11-9" fill="none" stroke="#3f7a4a" stroke-width="2"/></svg><span>hello@verrajuicery.example</span></li>
    </ul>
  </div>
  <div class="footer-rule"></div>
  <p class="copyright">© 2018 Company Name &nbsp;All right reserved &nbsp;Term of Use</p>
</footer>

</body>
</html>
```